Property Management Special Flyer - this month only deal

We need a flyer that's design aligns with the style of our website and regular price package attached.
We are a high quality service company that offers property management along Sydney's Northern Beaches.
This month we want to offer a deal where we are waiving Advertising Fees and a special management rate of 5% for this month (Aug) only.
Please show all the same details as on the "Tenancy and Upkeep Bundle" flyer but advertising the fact that this month only we are waiving the $350 advertising fee and a special Management fee of 5%.
I would like an A4 print ready version (with bleed if nec), an PDF version so we can email it to clients and an editable Photoshop PSD layered file so we can edit text if necessary for future use.
We would like to use the same background image as used in the price package flyer attached (background image also attached)
We want this flyer to capture attention but still look professional and clean like our website.

```html
<!DOCTYPE html>
<html lang="en">
<head>
<meta charset="utf-8">
<title>Tenancy and Upkeep Bundle – August Special</title>
<link href="https://fonts.googleapis.com/css2?family=Open+Sans:ital,wdth,wght@0,75..100,300..800;1,75..100,300..800&family=Source+Sans+3:ital,wght@0,400;0,600;0,700;1,700&display=swap" rel="stylesheet">
<style>
  :root{
    --teal:#1f9aa6;
    --teal-deep:#16707a;
    --teal-soft:#a9d5d9;
    --row-grey:#efeff0;
    --ink:#3a3d42;
    --ink-soft:#7b7f86;
    --footer:#3c3f45;
    --page:#ffffff;
    --stage:#e6e7e9;
  }
  *{box-sizing:border-box;margin:0;padding:0}
  html,body{width:1000px;height:1200px;overflow:hidden;background:var(--stage)}
  body{font-family:"Source Sans 3",Arial,sans-serif;color:var(--ink)}
  .flyer{position:absolute;left:90px;top:20px;width:820px;height:1160px;background:var(--page);overflow:hidden}

  .hero{position:absolute;left:0;top:0;width:820px;height:535px;
    background:linear-gradient(180deg,#1a86c9 0%,#5fb0de 30%,#c9cfd0 55%,#5d7a55 75%,#3e5a3e 100%)}
  .hero-title{position:absolute;left:0;top:462px;width:820px;height:73px;
    background:rgba(22,112,122,.82);color:#fff;font-family:"Open Sans",Arial,sans-serif;font-weight:300;font-size:38px;
    letter-spacing:.3px;text-align:center;line-height:73px}

  .includes{position:absolute;left:44px;top:570px;width:345px}
  .includes h2{font-family:"Open Sans",Arial,sans-serif;color:var(--teal);font-size:20px;font-weight:700;line-height:26px;margin-bottom:10px}
  .includes ul{list-style:none}
  .includes li{position:relative;padding-left:22px;font-size:16px;line-height:24.5px;color:var(--ink)}
  .includes li svg{position:absolute;left:0;top:6px;width:12px;height:12px}

  .gallery{position:absolute;left:396px;top:565px;width:376px;height:99px;display:flex;justify-content:space-between}
  .gallery .shot{width:120px;height:99px;border:3px solid var(--teal);padding:3px;background:#fff}
  .gallery .shot div{width:100%;height:100%}
  .shot-a div{background:linear-gradient(180deg,#3f8fd0,#7fb7dd 55%,#23648e)}
  .shot-b div{background:linear-gradient(180deg,#6fb0e0,#c8c4bb 50%,#5c7b4e)}
  .shot-c div{background:linear-gradient(180deg,#4a9ddb,#a6cde6 50%,#8a8a80)}

  .special-bar{position:absolute;left:396px;top:684px;width:376px;height:29px;background:var(--teal);
    color:#fff;font-family:"Open Sans",Arial,sans-serif;font-stretch:82%;font-weight:400;font-size:18px;
    line-height:29px;padding-left:12px;white-space:nowrap}

  .rates{position:absolute;left:396px;top:726px;width:376px;border-collapse:collapse;font-size:13.5px}
  .rates td{height:33.5px;padding:0 8px;vertical-align:middle;white-space:nowrap}
  .rates tr:nth-child(odd){background:var(--row-grey)}
  .rates tr:nth-child(even){background:var(--teal-soft)}
  .rates td.label{width:164px;color:var(--ink-soft)}
  .rates tr:nth-child(even) td.label{color:var(--ink)}
  .rates td.value{color:var(--ink);padding-left:2px}
  .rates td.value.strong{font-weight:600;color:#555a60}
  .rates td.value.tight{font-size:12px;letter-spacing:-.2px}

  .offer{position:absolute;left:396px;top:964px;width:376px;height:52px;background:var(--teal);color:#fff;
    font-family:"Open Sans",Arial,sans-serif;font-stretch:82%;font-weight:400;font-size:17px;line-height:21px;
    padding:5px 12px;text-transform:uppercase;white-space:nowrap}
  .offer em{font-weight:700;font-style:italic}

  .footer-rule{position:absolute;left:0;top:1037px;width:820px;height:5px;background:var(--teal)}
  .footer{position:absolute;left:0;top:1042px;width:820px;height:118px;background:var(--footer)}
  .brand{position:absolute;left:44px;top:44px;display:flex;align-items:center;gap:10px;color:#fff;
    font-family:"Open Sans",Arial,sans-serif;font-weight:700;font-size:22px;letter-spacing:.3px}
  .brand .dot{width:14px;height:14px;background:var(--teal)}
  .divider{position:absolute;left:407px;top:18px;width:1px;height:82px;background:#6a6e75}
  .contacts{position:absolute;left:432px;top:16px;color:#fff;font-size:14px;line-height:21px}
  .contacts p{display:flex;align-items:center;gap:6px;white-space:nowrap}
  .contacts svg{width:12px;height:12px;flex:none}
</style>
</head>
<body>
<main class="flyer">
  <div class="hero" role="img" aria-label="Photograph of a modern two-storey coastal home with glass balconies, terraced gardens and blue sky"></div>
  <h1 class="hero-title">TENANCY AND UPKEEP BUNDLE</h1>

  <section class="includes">
    <h2>INCLUDES:</h2>
    <ul>
      <li><svg viewBox="0 0 14 14"><circle cx="7" cy="7" r="7" fill="#1f9aa6"/><path d="M5.5 4l3 3-3 3" stroke="#fff" stroke-width="1.8" fill="none"/></svg>Securing Tenant</li>
      <li><svg viewBox="0 0 14 14"><circle cx="7" cy="7" r="7" fill="#1f9aa6"/><path d="M5.5 4l3 3-3 3" stroke="#fff" stroke-width="1.8" fill="none"/></svg>Reference/Database Checking</li>
      <li><svg viewBox="0 0 14 14"><circle cx="7" cy="7" r="7" fill="#1f9aa6"/><path d="M5.5 4l3 3-3 3" stroke="#fff" stroke-width="1.8" fill="none"/></svg>Lease Preparation and Signing</li>
      <li><svg viewBox="0 0 14 14"><circle cx="7" cy="7" r="7" fill="#1f9aa6"/><path d="M5.5 4l3 3-3 3" stroke="#fff" stroke-width="1.8" fill="none"/></svg>Direct Deposit rent collection</li>
      <li><svg viewBox="0 0 14 14"><circle cx="7" cy="7" r="7" fill="#1f9aa6"/><path d="M5.5 4l3 3-3 3" stroke="#fff" stroke-width="1.8" fill="none"/></svg>Zero arrears policy management</li>
      <li><svg viewBox="0 0 14 14"><circle cx="7" cy="7" r="7" fill="#1f9aa6"/><path d="M5.5 4l3 3-3 3" stroke="#fff" stroke-width="1.8" fill="none"/></svg>Payment of Rates and levies</li>
      <li><svg viewBox="0 0 14 14"><circle cx="7" cy="7" r="7" fill="#1f9aa6"/><path d="M5.5 4l3 3-3 3" stroke="#fff" stroke-width="1.8" fill="none"/></svg>Insurance management</li>
      <li><svg viewBox="0 0 14 14"><circle cx="7" cy="7" r="7" fill="#1f9aa6"/><path d="M5.5 4l3 3-3 3" stroke="#fff" stroke-width="1.8" fill="none"/></svg>Coordination or all repairs and maintenance</li>
      <li><svg viewBox="0 0 14 14"><circle cx="7" cy="7" r="7" fill="#1f9aa6"/><path d="M5.5 4l3 3-3 3" stroke="#fff" stroke-width="1.8" fill="none"/></svg>Regular rent reviews and renewals</li>
      <li><svg viewBox="0 0 14 14"><circle cx="7" cy="7" r="7" fill="#1f9aa6"/><path d="M5.5 4l3 3-3 3" stroke="#fff" stroke-width="1.8" fill="none"/></svg>Detailed ingoing, ongoing and outgoing<br>inspections with photos and videos – viewable<br>through your personal Landlord portal</li>
      <li><svg viewBox="0 0 14 14"><circle cx="7" cy="7" r="7" fill="#1f9aa6"/><path d="M5.5 4l3 3-3 3" stroke="#fff" stroke-width="1.8" fill="none"/></svg>Bond management – lodging and refunding</li>
      <li><svg viewBox="0 0 14 14"><circle cx="7" cy="7" r="7" fill="#1f9aa6"/><path d="M5.5 4l3 3-3 3" stroke="#fff" stroke-width="1.8" fill="none"/></svg>Electronic monthly and EOFY statements</li>
      <li><svg viewBox="0 0 14 14"><circle cx="7" cy="7" r="7" fill="#1f9aa6"/><path d="M5.5 4l3 3-3 3" stroke="#fff" stroke-width="1.8" fill="none"/></svg>Annual scheduled maintenance report</li>
      <li><svg viewBox="0 0 14 14"><circle cx="7" cy="7" r="7" fill="#1f9aa6"/><path d="M5.5 4l3 3-3 3" stroke="#fff" stroke-width="1.8" fill="none"/></svg>Regulation/compliance management</li>
      <li><svg viewBox="0 0 14 14"><circle cx="7" cy="7" r="7" fill="#1f9aa6"/><path d="M5.5 4l3 3-3 3" stroke="#fff" stroke-width="1.8" fill="none"/></svg>Tribunal Representation</li>
    </ul>
  </section>

  <div class="gallery">
    <div class="shot shot-a"><div role="img" aria-label="Photograph of a harbour with moored boats"></div></div>
    <div class="shot shot-b"><div role="img" aria-label="Photograph of modern homes along a leafy street"></div></div>
    <div class="shot shot-c"><div role="img" aria-label="Photograph of a seaside promenade"></div></div>
  </div>

  <div class="special-bar">SPECIAL RATE FOR THIS MONTH (AUG) ONLY.</div>

  <table class="rates">
    <tr><td class="label">Management Rate:</td><td class="value strong">5% + GST of rental income</td></tr>
    <tr><td class="label">Letting Fee:</td><td class="value tight">1weeks rent+GST 6 or 12month lease</td></tr>
    <tr><td class="label">Advertising:</td><td class="value strong">No Charge</td></tr>
    <tr><td class="label">Professional Photography:</td><td class="value">$199 (inc GST) 4 x Photos</td></tr>
    <tr><td class="label">Statements:</td><td class="value">$5.00 Per month</td></tr>
    <tr><td class="label">Lease Preperation:</td><td class="value">No Charge</td></tr>
    <tr><td class="label">Renewal Fees:</td><td class="value">½ Weeks Rent +GST</td></tr>
  </table>

  <div class="offer">We are waiving the <em>$350 advertising fee</em><br>and a special <em>management fee of 5%.</em></div>

  <div class="footer-rule"></div>
  <footer class="footer">
    <div class="brand"><span class="dot"></span>HARBOUR CREST AGENCY</div>
    <div class="divider"></div>
    <div class="contacts">
      <p>Tom Hale
        <svg viewBox="0 0 12 12"><circle cx="6" cy="6" r="5.3" fill="none" stroke="#1f9aa6" stroke-width="1.2"/><path d="M4 3.3l1 .2.4 1.4-.7.6a4 4 0 0 0 1.8 1.8l.6-.7 1.4.4.2 1c-2.8.6-5.3-1.9-4.7-4.7z" fill="#1f9aa6"/></svg>
        0400 117 208 | Nadia Corra
        <svg viewBox="0 0 12 12"><circle cx="6" cy="6" r="5.3" fill="none" stroke="#1f9aa6" stroke-width="1.2"/><path d="M4 3.3l1 .2.4 1.4-.7.6a4 4 0 0 0 1.8 1.8l.6-.7 1.4.4.2 1c-2.8.6-5.3-1.9-4.7-4.7z" fill="#1f9aa6"/></svg>
        0400 562 914</p>
      <p><svg viewBox="0 0 12 12"><path d="M6 11.5S2 7.2 2 4.6a4 4 0 0 1 8 0C10 7.2 6 11.5 6 11.5z" fill="#1f9aa6"/><circle cx="6" cy="4.6" r="1.4" fill="#3c3f45"/></svg>Suite 4, 18-20 Shore Parade, Bayview NSW 2104</p>
      <p><svg viewBox="0 0 12 12"><rect x="1" y="2.5" width="10" height="7" fill="none" stroke="#1f9aa6" stroke-width="1.1"/><path d="M1 2.5l5 4 5-4" fill="none" stroke="#1f9aa6" stroke-width="1.1"/></svg>hello@harbourcrestagency.com.au</p>
      <p><svg viewBox="0 0 12 12"><circle cx="6" cy="6" r="5" fill="none" stroke="#1f9aa6" stroke-width="1.1"/><ellipse cx="6" cy="6" rx="2.2" ry="5" fill="none" stroke="#1f9aa6" stroke-width="1"/><path d="M1 6h10" stroke="#1f9aa6" stroke-width="1"/></svg>www.harbourcrestagency.com.au</p>
    </div>
  </footer>
</main>
</body>
</html>
```